Clean Vormix Ads Banner Design For A Finance Company

Hi,
We're a UK based finance company and are looking for new banner ads to use on the Vormix Display Network.
We want the end product to stand out by using strong, minimal design - ideally starting from a dark theme, although I'm open to ideas.
The copy should read:
'Fast Bridging Loans From 0.39% PM'
Once we have these designs agreed, we are looking to replicate them for other products, changing only the text on each ad - for example, 'commercial mortgage service you can rely on' or 'development finance service you can rely on'.
The colours used on our website are the following:
Black - #040303
Orange - #f79124
White - #ffffff
Grey - #ffffff
Example ads that I like - https://www.plexabyte.com/wp-content/uploads/2021/07/vormix-display-ads-example-2-final.png.webp
2 - https://adquilterhub.com/wp-content/uploads/2020/03/fbdd56ba3bd16c7a8debb13a411de786.jpg

```html
<!DOCTYPE html>
<html lang="en">
<head>
<meta charset="utf-8">
<title>Fast Bridging Loans Banner</title>
<link rel="stylesheet" href="https://fonts.googleapis.com/css2?family=Archivo+Black&display=swap">
<style>
  :root {
    --page: #ffffff;
    --banner-bg: #1c1a1b;
    --orange: #ef4a04;
    --amber: #e8a10a;
    --slate: #333132;
    --cream: #f6e7dc;
    --white: #ffffff;
    --brand-orange: #f79124;
  }
  html, body {
    margin: 0;
    padding: 0;
    width: 1200px;
    height: 1200px;
    overflow: hidden;
    background: var(--page);
  }
  .canvas {
    position: relative;
    width: 1200px;
    height: 1200px;
    background: var(--page);
  }
  .banner {
    position: absolute;
    left: 0;
    top: 300px;
    width: 1200px;
    height: 600px;
    background: var(--banner-bg);
    overflow: hidden;
  }
  .banner-shapes {
    position: absolute;
    inset: 0;
    width: 1200px;
    height: 600px;
  }
  .headline {
    position: absolute;
    left: 535px;
    top: 254px;
    margin: 0;
    font-family: "Archivo Black", "Arial Black", sans-serif;
    font-weight: 400;
    font-size: 43px;
    line-height: 43px;
    letter-spacing: 2.4px;
    color: var(--cream);
    text-transform: uppercase;
  }
  .headline span { display: block; }
  .brand-box {
    position: absolute;
    left: 17px;
    top: 491px;
    width: 203px;
    height: 96px;
    background: var(--white);
    display: flex;
    align-items: center;
    justify-content: center;
  }
  .brand-name {
    font-family: "Archivo Black", "Arial Black", sans-serif;
    font-size: 21px;
    line-height: 24px;
    color: var(--brand-orange);
    text-align: center;
    letter-spacing: 0.5px;
  }
</style>
</head>
<body>
<div class="canvas">
  <section class="banner">
    <svg class="banner-shapes" viewBox="0 0 1200 600" xmlns="http://www.w3.org/2000/svg">
      <defs>
        <linearGradient id="photo-tone" x1="0" y1="0" x2="0.6" y2="1">
          <stop offset="0" stop-color="#6b4030"/>
          <stop offset="0.55" stop-color="#4a3029"/>
          <stop offset="1" stop-color="#2a2a2c"/>
        </linearGradient>
      </defs>

      <!-- top-left corner stripes -->
      <g class="corner-stripes-top">
        <polygon points="0,0 63.5,0 0,63.5" fill="var(--orange)"/>
        <polygon points="63.5,0 118.6,0 16.9,105.9 67.8,105.9 12.7,163 0,163 0,63.5" fill="var(--amber)"/>
        <polygon points="118.6,0 230,0 127,105.9 16.9,105.9" fill="var(--slate)"/>
      </g>

      <!-- top hexagon accent -->
      <g class="hex-accent-top">
        <polygon points="288,0 512.4,0 512.4,34 399.8,103.3 288,34" fill="var(--orange)" stroke="var(--orange)" stroke-width="8" stroke-linejoin="round"/>
        <polyline points="330.3,0 330.3,42.3 442,103.3 556.5,42.3 556.5,0" fill="none" stroke="var(--amber)" stroke-width="1.6"/>
      </g>

      <!-- dot grids -->
      <g class="dots-top-right" fill="var(--amber)">
        <circle cx="1075.7" cy="52" r="2.6"/><circle cx="1103.7" cy="52" r="2.6"/><circle cx="1131.7" cy="52" r="2.6"/><circle cx="1159.7" cy="52" r="2.6"/><circle cx="1187.7" cy="52" r="2.6"/>
        <circle cx="1075.7" cy="80" r="2.6"/><circle cx="1103.7" cy="80" r="2.6"/><circle cx="1131.7" cy="80" r="2.6"/><circle cx="1159.7" cy="80" r="2.6"/><circle cx="1187.7" cy="80" r="2.6"/>
        <circle cx="1075.7" cy="108" r="2.6"/><circle cx="1103.7" cy="108" r="2.6"/><circle cx="1131.7" cy="108" r="2.6"/><circle cx="1159.7" cy="108" r="2.6"/><circle cx="1187.7" cy="108" r="2.6"/>
        <circle cx="1075.7" cy="136" r="2.6"/><circle cx="1103.7" cy="136" r="2.6"/><circle cx="1131.7" cy="136" r="2.6"/><circle cx="1159.7" cy="136" r="2.6"/><circle cx="1187.7" cy="136" r="2.6"/>
      </g>
      <g class="dots-bottom-left" fill="var(--orange)">
        <circle cx="23.7" cy="471" r="2.6"/><circle cx="51.7" cy="471" r="2.6"/><circle cx="79.7" cy="471" r="2.6"/><circle cx="107.7" cy="471" r="2.6"/><circle cx="135.7" cy="471" r="2.6"/>
        <circle cx="23.7" cy="499" r="2.6"/><circle cx="51.7" cy="499" r="2.6"/><circle cx="79.7" cy="499" r="2.6"/><circle cx="107.7" cy="499" r="2.6"/><circle cx="135.7" cy="499" r="2.6"/>
        <circle cx="23.7" cy="527" r="2.6"/><circle cx="51.7" cy="527" r="2.6"/><circle cx="79.7" cy="527" r="2.6"/><circle cx="107.7" cy="527" r="2.6"/><circle cx="135.7" cy="527" r="2.6"/>
      </g>

      <!-- feature image hexagon -->
      <polygon class="feature-image" role="img" aria-label="Photo of a person at a desk with a small model house and loan paperwork" points="81.3,299 173.6,127 400.6,127 493,299 392,481.6 173.6,481.6" fill="url(#photo-tone)"/>

      <!-- bottom hexagon accent -->
      <g class="hex-accent-bottom">
        <polygon points="593.8,565 705.6,501 819,565 819,604 593.8,604" fill="var(--orange)" stroke="var(--orange)" stroke-width="8" stroke-linejoin="round"/>
        <polyline points="637,600 637,561.7 750.4,498.2 864,561.7 864,600" fill="none" stroke="var(--amber)" stroke-width="1.6"/>
      </g>

      <!-- bottom-right corner stripes -->
      <g class="corner-stripes-bottom">
        <polygon points="1169,420.3 1200,388 1200,420.3" fill="var(--orange)"/>
        <polygon points="1008,600 1105.3,420.3 1200,420.3 1200,456 1063,600" fill="var(--white)"/>
        <polygon points="896,600 1016.4,477 1128,477 1008,600" fill="var(--slate)"/>
        <polygon points="1063,600 1200,456 1200,538 1139,600" fill="var(--orange)"/>
        <polygon points="1139,600 1200,538 1200,600" fill="var(--amber)"/>
      </g>
    </svg>

    <h1 class="headline">
      <span>Fast Bridging Loans</span>
      <span>From 0.39% PM</span>
    </h1>

    <div class="brand-box">
      <div class="brand-name">Nordal Finance</div>
    </div>
  </section>
</div>
</body>
</html>
```